BRAVEN POWERLINE SERVICES needs a vibrant design for electrical contracting work.

I require a card design for my own electrical contracting business. I will be doing a lot of domestic and commercial work, including things such as repairs, maintenance, lighting, installations and various others. LED lighting and energy efficiency will be a big part of my business. I wish not to have childish pictures such as light bulbs in the design, but rather a smart and modern looking card which incorporates my logo colours and perhaps the same lighting strike within the faded background of the card.

Target Market(s)

Residential and Commercial property owners.

Industry/Entity Type

Electrical

Contact Information for Business Card

Dalen Voskic
EC40923
Phone Number: 0417 358 942
Email: dalen@bravenpowerline.com

Font styles to use
Serif
Sans Serif

Requirements
Must have
• My Logo and associated colours.
Nice to have
• Some form of shapes splitting the card into different colours related to the colours of my logo. Electric Blue, Silver/Grey and White.
Should not have
• Childish pictures and symbols such as light bulbs.

```html
<!DOCTYPE html>
<html lang="en">
<head>
<meta charset="utf-8">
<title>Braven Powerline Services – Business Card</title>
<link href="https://fonts.googleapis.com/css2?family=Lato:wght@400;700&display=swap" rel="stylesheet">
<style>
  :root {
    --backdrop: #e9e7e3;
    --card-white: #ffffff;
    --electric-blue: #3a4fa6;
    --electric-blue-deep: #2f4396;
    --logo-blue: #3c4fa8;
    --silver-light: #e4e6ea;
    --silver-dark: #8c9097;
    --text-on-blue: #ffffff;
  }
  * { margin: 0; padding: 0; box-sizing: border-box; }
  html, body {
    width: 1200px; height: 795px; overflow: hidden;
    background: var(--backdrop);
    font-family: "Lato", Arial, sans-serif;
  }
  .canvas { position: relative; width: 1200px; height: 795px; }
  .business-card {
    position: absolute; left: 150px; top: 140px;
    width: 900px; height: 514px;
    border-radius: 34px; overflow: hidden;
    background: var(--card-white);
    box-shadow: 0 10px 30px rgba(0,0,0,0.18);
  }
  .card-shapes { position: absolute; inset: 0; }
  .brand {
    position: absolute; left: 270px; top: 62px;
    display: flex; align-items: center; gap: 18px;
    color: var(--logo-blue); font-weight: 700;
  }
  .brand-dot {
    width: 62px; height: 62px; border-radius: 50%;
    background: var(--logo-blue); flex: none;
  }
  .brand-name { line-height: 1; }
  .brand-name .primary { display: block; font-size: 64px; letter-spacing: 3px; }
  .brand-name .secondary { display: block; font-size: 26px; letter-spacing: 2px; margin-top: 6px; }
  .holder {
    position: absolute; right: 560px; top: 240px;
    text-align: right; color: var(--text-on-blue);
  }
  .holder .name { font-size: 25px; font-weight: 700; }
  .holder .role { font-size: 23px; font-weight: 700; margin-top: 2px; }
  .holder .address { font-size: 20px; margin-top: 16px; line-height: 1.3; }
  .divider {
    position: absolute; left: 370px; top: 290px;
    width: 2px; height: 120px; background: rgba(255,255,255,0.75);
  }
  .contact-list {
    position: absolute; left: 396px; top: 318px;
    list-style: none; color: var(--text-on-blue); font-size: 21px;
  }
  .contact-list li { display: flex; align-items: center; gap: 10px; height: 27px; }
  .contact-list svg { width: 18px; height: 18px; flex: none; }
</style>
</head>
<body>
<div class="canvas">
  <div class="business-card">
    <svg class="card-shapes" viewBox="0 0 900 514" width="900" height="514" aria-hidden="true">
      <defs>
        <linearGradient id="silverEdge" x1="0" y1="0" x2="1" y2="0">
          <stop offset="0" stop-color="var(--silver-light)"/>
          <stop offset="0.5" stop-color="var(--silver-dark)"/>
          <stop offset="1" stop-color="var(--silver-light)"/>
        </linearGradient>
        <linearGradient id="blueBand" x1="0" y1="0" x2="1" y2="1">
          <stop offset="0" stop-color="var(--electric-blue)"/>
          <stop offset="1" stop-color="var(--electric-blue-deep)"/>
        </linearGradient>
      </defs>
      <path d="M0,168 C320,118 660,200 900,462 L900,514 L0,514 Z" fill="url(#silverEdge)"/>
      <path d="M0,178 C320,132 650,216 900,474 L900,514 L0,514 Z" fill="url(#blueBand)"/>
    </svg>

    <div class="brand">
      <span class="brand-dot"></span>
      <div class="brand-name">
        <span class="primary">BRAVEN</span>
        <span class="secondary">POWERLINE SERVICES</span>
      </div>
    </div>

    <div class="holder">
      <p class="name">Dalen Voskic</p>
      <p class="role">Job Title</p>
      <p class="address">00 Harbour Rd, Suite 900<br>Brisbane, QLD 4000</p>
    </div>

    <div class="divider"></div>

    <ul class="contact-list">
      <li>
        <svg viewBox="0 0 18 18" aria-hidden="true"><path d="M2 6c0-2 2-3 7-3s7 1 7 3v1h-4V5.5H6V7H2z M4 8h10l2 7H2z" fill="#fff"/></svg>
        0417 358 942
      </li>
      <li>
        <svg viewBox="0 0 18 18" aria-hidden="true"><rect x="4" y="2" width="10" height="5" fill="#fff"/><rect x="1" y="7" width="16" height="7" rx="1" fill="#fff"/><rect x="4" y="12" width="10" height="4" fill="#fff" stroke="#3a4fa6"/></svg>
        0417 358 943
      </li>
      <li>
        <svg viewBox="0 0 18 18" aria-hidden="true"><rect x="1" y="3" width="16" height="12" fill="#fff"/><path d="M1 3l8 7 8-7" fill="none" stroke="#3a4fa6" stroke-width="1.4"/></svg>
        dalen@bravenpowerline.com
      </li>
      <li>
        <svg viewBox="0 0 18 18" aria-hidden="true"><rect x="2" y="3" width="14" height="9" fill="none" stroke="#fff" stroke-width="1.6"/><rect x="6" y="14" width="6" height="1.8" fill="#fff"/></svg>
        www.bravenpowerline.com
      </li>
    </ul>
  </div>
</div>
</body>
</html>
```